We are a small NZ based company looking to rebrand our eco chem free cleaning product Brisko

This product was launched in 2021. The brand and labeling were aimed at the consumer who cared that the cleaning products they bought into their home were not only effective but non-harmful to their families and the environment. The label was a little bohemian/ natural. We feel that the labels now need to be more chic and classy, They need to look stylish in a country cottage as well as a high end minimalist home. Colours need to be mute so as to fit with most decors.
We need help with font colour and type - layout and balance. Trigger/ pump colour.
I have attached photos of our current range and labels
A couple of mock ups we are working on - (struggling with )
A colour pallet
The two last PNG files are closer to where we want to end up but they are not really right.

The products are sold online only
Our website is www.brisko.co.nz
The Brand board that we had done sometime ago is that last file.
Most of the colours on the labels are ok - except the apricot on the foaming hand soap bottle and the colour on the all purpose bottle - neither of which we love.
The Fair Harbour bottles are closer to what we are thinking.
Canva Links
https://www.draftpad.example/design/QWRTyu12abc/pLmNoPqRsTuVwXyZ12AbCd/edit
https://www.draftpad.example/design/QWRTzk34def/hGfEdCbAzYxWvUtSr34EfG/edit
https://www.draftpad.example/design/QWRTmn56ghi/tRsQpOnMlKjIhGfE56HiJk/edit
https://www.draftpad.example/design/QWRTbv78jkl/mNbVcXzLkJhGfDsA78LmNo/edit

Target Market(s)

Mothers who care about the products they bring into there homes but also want the product to look good in the home

Industry/Entity Type

Cleaning products

Requirements
Must have
• Design must be chic - and be able to sit and look great in any modern bathroom or kitchen.

```html
<!DOCTYPE html>
<html lang="en">
<head>
<meta charset="utf-8">
<title>Brisko – Concentrate Multi-Purpose Cleaner Label</title>
<link rel="stylesheet" href="https://fonts.googleapis.com/css2?family=Abril+Fatface&family=Cinzel:wght@600&family=Roboto+Slab:wght@300;400&family=Libre+Baskerville:wght@700&display=swap">
<style>
  :root {
    --apricot: #fbd291;
    --label: #f8f8f8;
    --ink: #0d0d0d;
    --white: #ffffff;
  }
  html, body {
    margin: 0;
    padding: 0;
    width: 1200px;
    height: 1200px;
    overflow: hidden;
    background: var(--apricot);
  }
  .canvas {
    position: relative;
    width: 1200px;
    height: 1200px;
    background: var(--apricot);
    border-radius: 22px;
    overflow: hidden;
  }
  .label {
    position: absolute;
    left: 96px;
    top: 321px;
    width: 1036px;
    height: 573px;
    background: var(--label);
    border-radius: 4px;
  }
  .brand {
    position: absolute;
    left: 0;
    right: 0;
    top: 356px;
    text-align: center;
    color: var(--ink);
  }
  .brand-dot {
    display: block;
    width: 62px;
    height: 62px;
    margin: 0 auto 14px;
    border-radius: 50%;
    background: var(--ink);
  }
  .brand-name {
    display: block;
    font-family: "Cinzel", serif;
    font-weight: 600;
    font-size: 46px;
    line-height: 52px;
    letter-spacing: 2px;
  }
  .product {
    position: absolute;
    left: 0;
    right: 0;
    top: 584px;
    text-align: center;
    color: var(--ink);
  }
  .product-title {
    margin: 0;
    font-family: "Abril Fatface", serif;
    font-weight: 400;
    font-size: 58px;
    line-height: 56px;
    letter-spacing: 0;
  }
  .product-type {
    margin: 0;
    font-family: "Roboto Slab", serif;
    font-weight: 300;
    font-size: 31px;
    line-height: 34px;
    letter-spacing: 0.5px;
  }
  .badge {
    position: absolute;
    left: 0;
    top: 0;
    width: 1200px;
    height: 1200px;
  }
  .badge-arc-text {
    font-family: "Libre Baskerville", serif;
    font-weight: 700;
    font-size: 15px;
    fill: var(--ink);
  }
  .badge-hashtag {
    font-family: "Roboto Slab", serif;
    font-weight: 400;
    font-size: 25px;
    fill: var(--white);
  }
  .badge-claims {
    font-family: "Libre Baskerville", serif;
    font-weight: 700;
    font-size: 10.5px;
    fill: var(--ink);
  }
</style>
</head>
<body>
<div class="canvas">
  <div class="label"></div>

  <div class="brand">
    <span class="brand-dot"></span>
    <span class="brand-name">Brisko</span>
  </div>

  <div class="product">
    <h1 class="product-title">CONCERTRATE</h1>
    <p class="product-type">MULTI-PURPOSE CLEANER</p>
  </div>

  <svg class="badge" viewBox="0 0 1200 1200" aria-label="Product values badge">
    <defs>
      <clipPath id="label-clip">
        <rect x="96" y="321" width="1036" height="573"/>
      </clipPath>
      <path id="value-arc" d="M419,945 A178,178 0 0 1 775,945" fill="none"/>
    </defs>
    <circle cx="601" cy="1106" r="275" fill="var(--apricot)" clip-path="url(#label-clip)"/>
    <text class="badge-arc-text" text-anchor="middle">
      <textPath href="#value-arc" startOffset="99">ECO</textPath>
    </text>
    <text class="badge-arc-text" text-anchor="middle">
      <textPath href="#value-arc" startOffset="198">Chemical Free</textPath>
    </text>
    <text class="badge-arc-text" text-anchor="middle">
      <textPath href="#value-arc" startOffset="342">Cruelty Free</textPath>
    </text>
    <text class="badge-arc-text" text-anchor="middle">
      <textPath href="#value-arc" startOffset="456">NZ Made</textPath>
    </text>
    <text class="badge-hashtag" x="601" y="858" text-anchor="middle">#BeToxinFree</text>
    <text class="badge-claims" x="600" y="883" text-anchor="middle" xml:space="preserve">HYPOALLERGENIC    GF    NUT FREE    VEGAN</text>
  </svg>
</div>
</body>
</html>
```